E-commerce- Online Web Design Project

Needed: Web Design for an e-commerce website based in Kuwait called : Wardoon - which is the equivalent to " Everything" This website will be selling everything from - Electronics & Computers, health & beauty products, video games, Home Goods, Pet Supplies, Baby & Toddler, etc. Sale section.( Front End)
Then you have the Back End ( where the vendors go to upload their products)
Along with the different pages that comes with the project of an online store- about us- contact page- live chat ( operator) etc.
Industry/Entity Type
E-Commerce
Look and feel

```html
<!DOCTYPE html>
<html lang="en">
<head>
<meta charset="utf-8">
<title>Wardoon – Shopping Cart For all Your Needs</title>
<link rel="stylesheet" href="https://fonts.googleapis.com/css2?family=Source+Sans+3:wght@400;600;700&display=swap">
<style>
:root{
  --ink:#23272d;
  --night:#262b33;
  --night-deep:#1b1f25;
  --night-soft:#353c46;
  --slate:#abafb8;
  --paper:#ffffff;
  --line:#d9dde3;
  --frost:#eef0f3;
  --sky:#bcd0e6;
  --sky-text:#cfdcea;
  --brand:#2f4f82;
}
*{box-sizing:border-box;margin:0;padding:0}
html,body{width:879px;height:1200px;overflow:hidden}
body{position:relative;background:var(--slate);font-family:"Source Sans 3",Arial,sans-serif;color:var(--ink)}
a{color:inherit;text-decoration:none}
h1,h2,h3{font-weight:400}
.header-bg{position:absolute;left:0;top:0;width:879px;height:178px;background:var(--paper)}
.service-bar{position:absolute;left:0;top:0;width:879px;height:25px;background:var(--night);color:#e9ecef;font-size:9px;text-align:right;padding:8px 37px 0 0}
.brand{position:absolute;left:62px;top:36px;width:80px;text-align:center}
.brand-mark{display:block;width:68px;height:68px;margin:0 auto 4px;background:var(--brand)}
.brand-name{font-size:19px;color:var(--brand)}
.hotline{position:absolute;left:461px;top:51px;font-size:18px;color:#222}
.account{position:absolute;top:34px;right:36px;font-size:11px;color:#222}
.account span{margin-left:22px}
.carts{position:absolute;top:77px;right:36px;font-size:11px;color:#222}
.main-nav{position:absolute;left:170px;top:97px;width:690px;height:115px;background:linear-gradient(var(--night-soft),var(--night) 40%);border-radius:10px 0 6px 0}
.main-nav ul{list-style:none;display:flex;position:absolute;left:42px;top:10px;font-size:13px;color:#dfe4ea}
.main-nav li{margin-right:24px}
.search{position:absolute;left:476px;top:9px;width:190px;height:20px;border-radius:10px;background:var(--night-deep)}
.search svg{position:absolute;right:7px;top:3px}
.sidebar{position:absolute;left:19px;top:148px;width:180px;height:463px;background:linear-gradient(90deg,var(--night),var(--night-soft));border-radius:8px 0 0 8px}
.sidebar h2{font-size:17px;color:var(--sky-text);margin:11px 0 0 16px}
.sidebar ul{list-style:none;margin:7px 0 0 26px}
.sidebar li{position:relative;height:25.8px;border-bottom:1px solid #c9ced5;font-size:12.5px;color:#fff;padding-top:2px;width:138px}
.sidebar li svg{position:absolute;right:9px;top:9px}
.content{position:absolute;left:183px;top:132px;width:665px;height:893px;background:var(--paper);border-radius:0 8px 0 0}
.hero{position:absolute;left:17px;top:16px;width:632px;height:223px;border:1px solid var(--sky);border-radius:8px;overflow:hidden;background:var(--paper)}
.hero-visual{position:absolute;left:0;top:0;width:420px;height:221px;
  background:
    radial-gradient(ellipse 120px 95px at 330px 100px,rgba(70,140,210,.55),rgba(70,140,210,0) 100%),
    radial-gradient(ellipse 150px 85px at 170px 125px,rgba(225,205,190,.7),rgba(225,205,190,0) 100%),
    linear-gradient(90deg,#eef1f4 0%,#f4f6f8 70%,rgba(255,255,255,0) 100%)}
.hero-title{position:absolute;left:414px;top:71px;font-size:24px;font-weight:600;line-height:31px;color:#1f2226}
.section-title{position:absolute;left:21px;font-size:15px;color:#222;display:flex;align-items:center;width:626px}
.section-title::after{content:"";flex:1;height:1px;background:var(--line);margin-left:10px}
.section-title::before{content:"";position:absolute;right:-2px;top:8px;width:6px;height:6px;border-radius:50%;background:var(--line)}
.grid{position:absolute;left:21px;display:grid;grid-template-columns:repeat(4,144px);column-gap:16.7px;row-gap:17px}
.card{position:relative;width:144px;height:168px;border:1px solid var(--line);border-radius:8px;background:linear-gradient(#fff 40%,var(--frost));overflow:hidden}
.card-photo{position:absolute;left:8px;top:8px;width:128px;height:118px}
.card-name{position:absolute;left:9px;top:127px;font-size:12px;color:#222}
.card-bar{position:absolute;left:0;bottom:0;width:144px;height:22px;background:var(--night);border-radius:0 0 8px 8px}
.card-bar .cart{position:absolute;left:14px;top:4px;width:32px;height:14px;border-radius:7px;background:#fff}
.card-bar .cart svg{position:absolute;left:10px;top:2px}
.card-bar .view{position:absolute;right:14px;top:3px;font-size:11px;color:#e6eaee}
.pager{position:absolute;right:20px;top:864px;display:flex;gap:2px;font-size:13px;color:#222}
.pager span{width:12px;text-align:center}
.pager .current{background:var(--sky)}
.footer{position:absolute;left:0;top:1025px;width:879px;height:175px;background:linear-gradient(var(--night-soft),var(--night) 40%,var(--night-deep))}
.footer-col{position:absolute;top:27px;color:#fff}
.footer-col h3{font-size:13px;font-weight:600;margin-bottom:11px}
.footer-col ul{list-style:none;font-size:11px;color:#e3e6ea;margin-left:4px}
.footer-col li{height:19px}
.social{position:absolute;left:741px;top:109px;display:flex;gap:12px}
.social span{width:17px;height:17px;border-radius:3px}
.copyright{position:absolute;left:687px;top:140px;font-size:10px;color:#e3e6ea}
</style>
</head>
<body>
<svg width="0" height="0" style="position:absolute">
  <symbol id="cart-icon" viewBox="0 0 12 10"><path d="M0 1h2l2 6h6l1.5-4.5H3" fill="none" stroke="#222" stroke-width="1.3"/><circle cx="5" cy="9" r="1" fill="#222"/><circle cx="9" cy="9" r="1" fill="#222"/></symbol>
  <symbol id="chevron" viewBox="0 0 6 10"><path d="M1 1l4 4-4 4" fill="none" stroke="#fff" stroke-width="1.3"/></symbol>
</svg>

<div class="header-bg"></div>
<div class="service-bar">24 Hours Dispatch | Cash on Delivery | 30 Day Returns</div>

<a class="brand" href="#"><span class="brand-mark"></span><span class="brand-name">Wardoon</span></a>
<p class="hotline">Call Us On : 9876543210</p>
<p class="account">Welcome <span>Login / Sign Up</span></p>
<p class="carts">Wishlist &nbsp;(0) &nbsp;| &nbsp;Shopping Cart (0)</p>

<nav class="main-nav">
  <ul><li>Products</li><li>Suppliers</li><li>Sell Offers</li><li>Buy Leads</li></ul>
  <div class="search"><svg width="14" height="14" viewBox="0 0 14 14"><circle cx="5.5" cy="5.5" r="4" fill="none" stroke="#fff" stroke-width="1.6"/><line x1="8.5" y1="8.5" x2="13" y2="13" stroke="#fff" stroke-width="2"/></svg></div>
</nav>

<aside class="sidebar">
  <h2>Categories</h2>
  <ul>
    <li>Video games<svg width="6" height="10"><use href="#chevron"/></svg></li>
    <li>Home applicances<svg width="6" height="10"><use href="#chevron"/></svg></li>
    <li>Pet products<svg width="6" height="10"><use href="#chevron"/></svg></li>
    <li>Baby goods<svg width="6" height="10"><use href="#chevron"/></svg></li>
    <li>Video games<svg width="6" height="10"><use href="#chevron"/></svg></li>
    <li>Home applicances<svg width="6" height="10"><use href="#chevron"/></svg></li>
    <li>Pet products<svg width="6" height="10"><use href="#chevron"/></svg></li>
    <li>Baby goods<svg width="6" height="10"><use href="#chevron"/></svg></li>
  </ul>
</aside>

<main class="content">
  <section class="hero">
    <div class="hero-visual" role="img" aria-label="Tablets with blue covers showing a video call"></div>
    <h1 class="hero-title">Hello, we are a<br>Shopping Cart<br>For all Your Needs</h1>
  </section>

  <h2 class="section-title" style="top:253px">New Arrivals</h2>
  <div class="grid" style="top:280px">
    <article class="card"><div class="card-photo" role="img" aria-label="Stack of video game boxes" style="background:radial-gradient(ellipse 40% 45% at 55% 45%,#a9bba3,rgba(169,187,163,0))"></div><p class="card-name">Video games</p><div class="card-bar"><span class="cart"><svg width="12" height="10"><use href="#cart-icon"/></svg></span><span class="view">view</span></div></article>
    <article class="card"><div class="card-photo" role="img" aria-label="Metal pet bowl filled with dry food" style="background:radial-gradient(ellipse 48% 28% at 50% 55%,#b99566,rgba(185,149,102,0))"></div><p class="card-name">Pet Products</p><div class="card-bar"><span class="cart"><svg width="12" height="10"><use href="#cart-icon"/></svg></span><span class="view">view</span></div></article>
    <article class="card"><div class="card-photo" role="img" aria-label="Three-wheeled baby stroller" style="background:radial-gradient(ellipse 40% 48% at 52% 50%,#6e6f66,rgba(110,111,102,0))"></div><p class="card-name">Baby Products</p><div class="card-bar"><span class="cart"><svg width="12" height="10"><use href="#cart-icon"/></svg></span><span class="view">view</span></div></article>
    <article class="card"><div class="card-photo" role="img" aria-label="Stainless steel microwave oven" style="background:radial-gradient(ellipse 50% 34% at 50% 50%,#9a9ea3,rgba(154,158,163,0))"></div><p class="card-name">Oven</p><div class="card-bar"><span class="cart"><svg width="12" height="10"><use href="#cart-icon"/></svg></span><span class="view">view</span></div></article>
  </div>

  <h2 class="section-title" style="top:473px">Product Offers</h2>
  <div class="grid" style="top:502px">
    <article class="card"><div class="card-photo" role="img" aria-label="Open laptop computer" style="background:radial-gradient(ellipse 46% 40% at 50% 50%,#575e69,rgba(87,94,105,0))"></div><p class="card-name">Video games</p><div class="card-bar"><span class="cart"><svg width="12" height="10"><use href="#cart-icon"/></svg></span><span class="view">view</span></div></article>
    <article class="card"><div class="card-photo" role="img" aria-label="Studded pink and blue pet collars" style="background:radial-gradient(ellipse 50% 30% at 50% 45%,#d9a3bd,rgba(217,163,189,0)),radial-gradient(ellipse 45% 25% at 45% 60%,#9fbfe0,rgba(159,191,224,0))"></div><p class="card-name">Pet Products</p><div class="card-bar"><span class="cart"><svg width="12" height="10"><use href="#cart-icon"/></svg></span><span class="view">view</span></div></article>
    <article class="card"><div class="card-photo" role="img" aria-label="Colourful baby walker" style="background:radial-gradient(ellipse 30% 25% at 50% 35%,#e6c64f,rgba(230,198,79,0)),radial-gradient(ellipse 48% 30% at 50% 62%,#d8443f,rgba(216,68,63,0))"></div><p class="card-name">Baby Products</p><div class="card-bar"><span class="cart"><svg width="12" height="10"><use href="#cart-icon"/></svg></span><span class="view">view</span></div></article>
    <article class="card"><div class="card-photo" role="img" aria-label="Blender and food processor" style="background:radial-gradient(ellipse 22% 40% at 32% 50%,#a8737b,rgba(168,115,123,0)),radial-gradient(ellipse 25% 35% at 70% 55%,#5c6066,rgba(92,96,102,0))"></div><p class="card-name">Oven</p><div class="card-bar"><span class="cart"><svg width="12" height="10"><use href="#cart-icon"/></svg></span><span class="view">view</span></div></article>
    <article class="card"><div class="card-photo" role="img" aria-label="Natural care products in jars and a drawstring bag" style="background:radial-gradient(ellipse 45% 42% at 52% 52%,#d5b877,rgba(213,184,119,0))"></div><p class="card-name">Video games</p><div class="card-bar"><span class="cart"><svg width="12" height="10"><use href="#cart-icon"/></svg></span><span class="view">view</span></div></article>
    <article class="card"><div class="card-photo" role="img" aria-label="Patterned blue pet bowl" style="background:radial-gradient(ellipse 48% 28% at 50% 48%,#5d7cc8,rgba(93,124,200,0))"></div><p class="card-name">Pet Products</p><div class="card-bar"><span class="cart"><svg width="12" height="10"><use href="#cart-icon"/></svg></span><span class="view">view</span></div></article>
    <article class="card"><div class="card-photo" role="img" aria-label="Three-wheeled baby stroller" style="background:radial-gradient(ellipse 40% 48% at 52% 50%,#6e6f66,rgba(110,111,102,0))"></div><p class="card-name">Baby Products</p><div class="card-bar"><span class="cart"><svg width="12" height="10"><use href="#cart-icon"/></svg></span><span class="view">view</span></div></article>
    <article class="card"><div class="card-photo" role="img" aria-label="Top-loading washing machine" style="background:radial-gradient(ellipse 32% 48% at 50% 50%,#a4a9ae,rgba(164,169,174,0))"></div><p class="card-name">Oven</p><div class="card-bar"><span class="cart"><svg width="12" height="10"><use href="#cart-icon"/></svg></span><span class="view">view</span></div></article>
  </div>

  <nav class="pager"><span class="current">1</span><span>2</span><span>3</span><span>4</span><span>5</span></nav>
</main>

<footer class="footer">
  <div class="footer-col" style="left:48px"><h3>Video games</h3><ul><li>Video games</li><li>Home applicances</li><li>Pet products</li><li>Baby goods</li></ul></div>
  <div class="footer-col" style="left:181px"><h3>Home applicances</h3><ul><li>Video games</li><li>Home applicances</li><li>Pet products</li><li>Baby goods</li></ul></div>
  <div class="footer-col" style="left:345px"><h3>Pet products</h3><ul><li>Video games</li><li>Home applicances</li><li>Pet products</li><li>Baby goods</li></ul></div>
  <div class="footer-col" style="left:478px"><h3>Baby goods</h3><ul><li>Video games</li><li>Home applicances</li><li>Pet products</li><li>Baby goods</li></ul></div>
  <div class="social" aria-label="Social links"><span style="background:#4a4f57"></span><span style="background:#3ba3d8"></span><span style="background:#3b5c9a"></span><span style="background:#e8762c"></span></div>
  <p class="copyright">All Rights Reserved, ©2012 Wardoon</p>
</footer>
</body>
</html>
```